Store Fixture business needs a buisness card design

We are looking for a business card design for a store fixture company. "KL Shelf Outfitters" we help small businesses with their start up by providing fixtures required to display their products.
It should have a simple yet innovative design in the front, and a refined look to our company.
We would like our logo, to have one of our products "display cases, clothing rack, mannequins" integrated in the design. And the rest of it just a clean look, which gives our address, store hours, and contact number, etc.
The color scheme as seen in the samples can be changed as long as the goal is achieved.
Industry/Entity Type
Business
Contact Information for Business Card
KL Shelf Outfitters
4362 Marlow Ave.
San Antonio,TX 78299
www.klshelfoutfitters.example
klpo@klshelfoutfitter.example
(210) 555-0188
M-F: 9-6pm
Sat: 10-3pm

```html
<!DOCTYPE html>
<html lang="en">
<head>
<meta charset="utf-8">
<title>KL Shelf Outfitters – Business Card</title>
<link href="https://fonts.googleapis.com/css2?family=Arimo:wght@400;700&family=Tinos&display=swap" rel="stylesheet">
<style>
  :root {
    --backdrop: #d8d3cb;
    --card-black: #0c0c0c;
    --band-light: #e4e4e4;
    --band-mid: #c9c9c9;
    --name-grey: #6f6f6f;
    --accent-yellow: #f2c21b;
    --accent-magenta: #d634c8;
    --accent-blue: #2aa3dc;
    --accent-grey: #a9a9a9;
    --accent-orange: #e0522a;
    --accent-purple: #6b2a8c;
    --text-white: #ffffff;
    --hours-gold: #e2b62c;
  }
  * { box-sizing: border-box; margin: 0; padding: 0; }
  html, body { width: 1200px; height: 892px; overflow: hidden; }
  body {
    background: var(--backdrop);
    position: relative;
    font-family: "Arimo", Arial, sans-serif;
  }
  .card {
    position: absolute;
    top: 106px;
    width: 400px;
    height: 680px;
    background: var(--card-black);
    overflow: hidden;
    box-shadow: 0 10px 30px rgba(0,0,0,.35);
  }
  .card--contact { left: 150px; }
  .card--services { left: 650px; }

  .product-photo {
    position: absolute;
    background: radial-gradient(ellipse at 60% 55%, #d9d2c2 0%, #8c8478 30%, #2a2a2a 60%, var(--card-black) 80%);
  }
  .card--contact .product-photo { left: 30px; top: 20px; width: 350px; height: 220px; }
  .card--services .product-photo { left: 120px; top: 0; width: 280px; height: 320px; }

  .brand-band {
    position: absolute;
    left: 0; right: 0;
    background: linear-gradient(180deg, var(--band-light), var(--band-mid));
    display: flex;
    align-items: center;
    gap: 16px;
    padding: 0 28px;
  }
  .card--contact .brand-band { top: 250px; height: 120px; }
  .card--services .brand-band { top: 330px; height: 110px; }
  .brand-mark {
    width: 46px; height: 46px;
    background: var(--accent-yellow);
    flex: none;
  }
  .brand-name {
    font-weight: 700;
    font-size: 30px;
    line-height: 1.05;
    color: var(--name-grey);
    text-transform: uppercase;
    letter-spacing: 1px;
  }

  .contact-list {
    position: absolute;
    left: 0; right: 0; top: 382px;
    list-style: none;
  }
  .contact-bar {
    height: 50px;
    margin-bottom: 8px;
    display: flex;
    align-items: center;
    gap: 14px;
    padding-left: 14px;
    color: var(--text-white);
    font-weight: 700;
    font-size: 19px;
  }
  .contact-bar--phone { background: var(--accent-magenta); font-size: 22px; }
  .contact-bar--email { background: var(--accent-blue); }
  .contact-bar--web { background: var(--accent-yellow); }
  .contact-bar--address { background: var(--accent-grey); height: 70px; font-size: 18px; line-height: 1.25; }
  .contact-icon {
    width: 28px; height: 28px;
    border-radius: 50%;
    background: var(--card-black);
    flex: none;
    display: flex; align-items: center; justify-content: center;
  }
  .contact-icon svg { width: 15px; height: 15px; fill: var(--text-white); }

  .service-list {
    position: absolute;
    left: 34px; top: 458px;
    list-style: none;
    font-family: "Tinos", "Times New Roman", serif;
    color: var(--text-white);
    font-size: 25px;
    line-height: 1.22;
  }
  .service-list li { display: flex; align-items: center; gap: 14px; }
  .service-list li::before {
    content: "";
    width: 11px; height: 11px;
    border-radius: 50%;
    background: var(--accent-yellow);
  }
  .store-hours {
    position: absolute;
    left: 60px; top: 604px;
    font-family: "Tinos", "Times New Roman", serif;
    color: var(--hours-gold);
    font-size: 24px;
    line-height: 1.15;
  }
  .color-strip {
    position: absolute;
    left: 0; right: 0; bottom: 0;
    height: 14px;
    display: flex;
  }
  .color-strip span { flex: 1; }
  .color-strip .strip-yellow { background: var(--accent-yellow); }
  .color-strip .strip-orange { background: var(--accent-orange); }
  .color-strip .strip-purple { background: var(--accent-purple); }
</style>
</head>
<body>

<section class="card card--contact">
  <div class="product-photo" role="img" aria-label="Photo of store fixtures: white gondola shelving unit, red display case and dress-form mannequin on stand"></div>
  <div class="brand-band">
    <span class="brand-mark"></span>
    <span class="brand-name">KL Shelf<br>Outfitters</span>
  </div>
  <ul class="contact-list">
    <li class="contact-bar contact-bar--phone">
      <span class="contact-icon"><svg viewBox="0 0 24 24"><path d="M6.6 10.8a15.1 15.1 0 0 0 6.6 6.6l2.2-2.2c.3-.3.7-.4 1-.2 1.1.4 2.3.6 3.6.6.6 0 1 .4 1 1V20c0 .6-.4 1-1 1A17 17 0 0 1 3 4c0-.6.4-1 1-1h3.5c.6 0 1 .4 1 1 0 1.3.2 2.5.6 3.6.1.3 0 .7-.2 1z"/></svg></span>
      (210) 555-0188
    </li>
    <li class="contact-bar contact-bar--email">
      <span class="contact-icon"><svg viewBox="0 0 24 24"><path d="M2 5h20v14H2zM3.5 6.5 12 13l8.5-6.5z"/></svg></span>
      klpo@klshelfoutfitter.example
    </li>
    <li class="contact-bar contact-bar--web">
      <span class="contact-icon"><svg viewBox="0 0 24 24"><path d="M12 2a10 10 0 1 0 0 20 10 10 0 0 0 0-20zm0 2c1 0 2.3 2 2.8 5H9.2C9.7 6 11 4 12 4zm-7.5 7h4.3a17 17 0 0 0 0 2H4.5a8 8 0 0 1 0-2zm6.3 0h2.4a15 15 0 0 1 0 2h-2.4a15 15 0 0 1 0-2zm4.4 0h4.3a8 8 0 0 1 0 2h-4.3a17 17 0 0 0 0-2zM9.2 15h5.6c-.5 3-1.8 5-2.8 5s-2.3-2-2.8-5z"/></svg></span>
      www.klshelfoutfitters.example
    </li>
    <li class="contact-bar contact-bar--address">
      <span class="contact-icon"><svg viewBox="0 0 24 24"><path d="M12 2a7 7 0 0 0-7 7c0 5 7 13 7 13s7-8 7-13a7 7 0 0 0-7-7zm0 9.5a2.5 2.5 0 1 1 0-5 2.5 2.5 0 0 1 0 5z"/></svg></span>
      <span>4362 Marlow Ave. San Antonio,<br>TX 78299</span>
    </li>
  </ul>
</section>

<section class="card card--services">
  <div class="product-photo" role="img" aria-label="Photo of a white dress-form mannequin on a black stand"></div>
  <div class="brand-band">
    <span class="brand-mark"></span>
    <span class="brand-name">KL Shelf<br>Outfitters</span>
  </div>
  <ul class="service-list">
    <li>Store Fixtures</li>
    <li>Display Fixtures</li>
    <li>Display Cases</li>
    <li>Gondola Shelving</li>
  </ul>
  <p class="store-hours">M-F: 9-6pm<br>Sat: 10-3pm</p>
  <div class="color-strip">
    <span class="strip-yellow"></span>
    <span class="strip-orange"></span>
    <span class="strip-purple"></span>
  </div>
</section>

</body>
</html>
```